Corporate speaking flyer for email

Redesign existing and very lame flyer. This is for my speaking business to be used as an introduction of content and style and my presentations. More photos can be provided. As you will see I'm an adventurer who makes part of my living from speaking about my adventures. The bio describes the general gist of that. There is more I could say but wanting to keep it pretty brief so as not to bore potential clients. Having said that I'd like to try and capture them in the first instance.

Target Market(s)

Corporate, clubs, events

Industry/Entity Type

Business

Requirements
Must have
• bio and references. Content provided. Feel free to edit.
Nice to have
• Surprise me!
Should not have
• Rude words.

```html
<!DOCTYPE html>
<html lang="en">
<head>
<meta charset="utf-8">
<title>Sam Calder – Speaker Flyer</title>
<link rel="stylesheet" href="https://fonts.googleapis.com/css2?family=Bebas+Neue&family=Open+Sans:ital,wght@0,400;1,700&display=swap">
<style>
  :root {
    --navy: #15213f;
    --orange: #fbb03b;
    --white: #ffffff;
    --photo-dark: #2b2926;
    --photo-mid: #5a554d;
    --sea: #6fa6c9;
    --street: #7a8a6a;
  }
  * { margin: 0; padding: 0; box-sizing: border-box; }
  html, body { width: 848px; height: 1200px; overflow: hidden; background: var(--white); }
  .flyer {
    position: relative; width: 848px; height: 1200px; overflow: hidden;
    font-family: "Open Sans", Arial, sans-serif;
  }
  .hero-photo {
    position: absolute; left: 0; top: 0; width: 848px; height: 760px;
    background: radial-gradient(ellipse at 70% 30%, var(--photo-mid) 0%, var(--photo-dark) 55%, #151412 100%);
  }
  .backdrop { position: absolute; inset: 0; }
  .title-banner {
    position: absolute; left: 17px; top: 20px; width: 602px; height: 92px;
    background: var(--orange);
    clip-path: polygon(0 0, 96% 0, 100% 100%, 0 100%);
    color: var(--navy);
    font-family: "Bebas Neue", "Oswald", sans-serif;
    font-size: 72px; line-height: 96px; padding-left: 10px; letter-spacing: 0.5px;
  }
  .testimonials {
    position: absolute; left: 20px; top: 124px; width: 560px; height: 620px;
    color: var(--white); font-size: 14.6px; line-height: 20.4px;
  }
  .testimonials .edge {
    float: right; width: 560px; height: 620px;
    shape-outside: polygon(410px 0, 100% 0, 100% 100%, 540px 100%);
  }
  .quote { text-align: justify; }
  .cite {
    display: block; color: var(--orange); font-style: italic; font-weight: 700;
    margin-bottom: 10px; text-align: left;
  }
  .field-photo {
    position: absolute; left: 0; top: 752px; width: 454px; height: 314px;
    background: var(--white); padding: 14px 18px 16px 18px;
  }
  .field-photo div {
    width: 100%; height: 100%;
    background: linear-gradient(135deg, var(--street) 0%, #9a9a90 45%, #5b5f55 100%);
  }
  .bio-photo {
    position: absolute; left: 440px; top: 676px; width: 390px; height: 200px;
    background: linear-gradient(180deg, var(--sea) 0%, #3d7fa8 60%, #d7dde2 100%);
  }
  .bio-heading {
    position: absolute; left: 434px; top: 800px; width: 98px; height: 76px;
    background: var(--white); color: var(--navy);
    font-family: "Bebas Neue", "Oswald", sans-serif; font-size: 66px; line-height: 80px;
    text-align: center;
  }
  .bio {
    position: absolute; left: 462px; top: 882px; width: 372px;
    color: var(--navy); font-size: 13.2px; line-height: 18.6px; text-align: justify;
  }
  .bio p { margin-bottom: 14px; }
  .bio p:nth-child(2) { margin-left: 14px; }
  .bio p:nth-child(3) { margin-left: 26px; }
  .contact {
    position: absolute; left: 25px; top: 1088px;
    color: var(--white); font-size: 20px; line-height: 25px;
  }
</style>
</head>
<body>
<main class="flyer">
  <div class="hero-photo" role="img" aria-label="Portrait of the speaker against a dark concrete wall"></div>

  <svg class="backdrop" width="848" height="1200" viewBox="0 0 848 1200" aria-hidden="true">
    <polygon points="0,0 420,0 558,705 0,705" fill="var(--navy)"/>
    <polygon points="0,700 560,700 440,1200 0,1200" fill="var(--navy)"/>
    <polygon points="420,745 848,664 848,1200 440,1200" fill="var(--orange)"/>
    <polygon points="452,752 848,690 848,1200 482,1200" fill="var(--white)"/>
    <polygon points="0,1175 440,1160 436,1200 0,1200" fill="var(--orange)"/>
  </svg>

  <h1 class="title-banner">What clients are saying .....</h1>

  <section class="testimonials">
    <div class="edge"></div>
    <p class="quote">“Sam has a remarkable story, told in a clever and compelling way. He is able to engage deeply with his audience; he made us laugh, cry and most importantly think deeply, as leaders, about our role in the world. One of the best!”</p>
    <span class="cite">Nora Pike, HR Manager, Greenfield Dairy</span>
    <p class="quote">You are the second only speaker who made me cry and laugh and feel great all in one short time period, thank you so much for everything you do, and have done…..</p>
    <span class="cite">Megan Ellis, Harbour Watch conference attendee</span>
    <p class="quote">“Kids Hope Trust was looking for an inspirational speaker who would reflect the passion, the hope and the commitment exhibited by KHT and its members. When I set out to look for such a person Sam Calder’s name kept bubbling to the surface and I’m delighted I made the phone call. Sam your speech is probably the most inspiring talk I have ever listened to. Your story is an amazing one delivered in a passionate and yet entertaining manner.”</p>
    <span class="cite">Tom Beaton, CEO Southport Regional Airport</span>
    <p class="quote">“… hearing your story was more inspirational than all the traditional "motivational" type trainers put together.”</p>
    <span class="cite">Dan Whitlow, Whitlow Property</span>
    <p class="quote">“The speaker was one of the most powerful I have listened to in years......incredible!”</p>
    <span class="cite">From client taken from conference feedback form</span>
    <p class="quote">Sam was unbelievable, amazing, so well received, such a lovely guy, so humble. Had some of the audience in tears.</p>
    <span class="cite">Grant Moffat, Kestrel Insurance Country Head</span>
  </section>

  <figure class="field-photo">
    <div role="img" aria-label="The speaker greeting an elderly man with a bouquet of lotus flowers while a camera crew films"></div>
  </figure>

  <div class="bio-photo" role="img" aria-label="Two rowers celebrating in their ocean rowing boat at the finish"></div>
  <h2 class="bio-heading">Bio</h2>

  <section class="bio">
    <p>Marathon rowing champion Sam Calder numerous achievements include World Champs silver, Commonwealth gold and a world record on the indoor rowing machine.</p>
    <p>Sam represented New Zealand at the Atlanta Olympics and published ‘The Long Pull’ on how he and Ben Tolley captured headlines around the world winning the grueling and inaugural Transatlantic Ocean Race in 41 days.</p>
    <p>Sam recently produced the award winning film Brother’s Road following his brother Kieran’s journey into Cambodia’s Khmer Rouge genocide. Powerful inspiring messages on tenacity, hope, love and the last human freedom: the power to choose your attitude and how you respond in a given situation.</p>
  </section>

  <address class="contact" style="font-style: normal;">
    +64 (0)21 555 01234<br>
    sam@swellmail.co.nz<br>
    www.samcalder.com
  </address>
</main>
</body>
</html>
```